Website Header for new website

We need a header/banner design for our revised website. Here is the link to our existing website lorimentaskel.me and to our new website in process seasonbrightway.us
Area of expertise is older adults, baby boomers and caregivers
This is an individual, professional website for a Speaker, Keynoter, Author, Brocaster

Target Market(s)

Event planners, broadcasters, publishers

Font styles to use
Serif

```html
<!DOCTYPE html>
<html lang="en">
<head>
<meta charset="utf-8">
<title>Lori Mentaskel — Website Header</title>
<link href="https://fonts.googleapis.com/css2?family=Pinyon+Script&family=Cabin:wght@500;700&display=swap" rel="stylesheet">
<style>
  :root{
    --canvas:#8c8c8c;
    --white:#ffffff;
    --orange-deep:#b9481f;
    --orange-mid:#d86a3c;
    --orange-light:#e89066;
    --slate:#2f3e4a;
    --band:rgba(196,138,128,0.82);
    --pill-fill:rgba(255,220,200,0.28);
    --pill-line:rgba(255,230,215,0.75);
  }
  *{margin:0;padding:0;box-sizing:border-box}
  html,body{width:1200px;height:1200px;overflow:hidden;background:var(--canvas)}
  body{position:relative;font-family:"Cabin",sans-serif}
  .header-variant{position:absolute;left:103px;width:994px}
  .header-variant.first{top:228px}
  .header-variant.second{top:637px}
  .nav-strip{height:65px;background:var(--white)}
  .hero{position:relative;height:290px;overflow:hidden;
    background:radial-gradient(ellipse at 60% 40%,var(--orange-light) 0%,var(--orange-mid) 45%,var(--orange-deep) 100%)}
  .portrait{position:absolute;left:0;top:0;width:341px;height:290px;
    background:linear-gradient(180deg,#cf7a4f 0%,#c9582c 55%,#3e3e40 78%,#2f2f31 100%)}
  .name{position:absolute;left:353px;top:4px;font-family:"Pinyon Script",serif;font-size:94px;font-weight:400;
    color:var(--slate);line-height:1.1;white-space:nowrap;
    text-shadow:1px 1px 0 #fff,-1px -1px 0 #fff,1px -1px 0 #fff,-1px 1px 0 #fff}
  .role{position:absolute;background:var(--pill-fill);border:1px solid var(--pill-line);border-radius:5px;
    color:var(--white);font-size:18px;font-weight:500;line-height:24px;padding:0 7px;white-space:nowrap}
  .row-1{top:143px}
  .row-2{top:183px}
  .col-a{left:354px}
  .col-b{left:551px}
  .col-c{left:747px}
  .col-b2{left:510px}
  .col-c2{left:712px}
  .featured-band{position:absolute;left:341px;right:0;top:234px;height:56px;background:var(--band);
    display:flex;align-items:center;padding:0 42px 0 36px;gap:18px}
  .second .featured-band{padding-left:14px;padding-right:64px}
  .featured-label{flex:none;border:1.5px dashed #fff;border-radius:5px;color:#fff;font-weight:700;font-size:19px;
    padding:2px 8px;white-space:nowrap}
  .outlets{flex:1;display:flex;justify-content:space-between;align-items:center;min-width:0}
  .outlet{color:var(--slate);font-size:12px;font-weight:700;white-space:nowrap}
</style>
</head>
<body>
  <section class="header-variant first">
    <div class="nav-strip"></div>
    <div class="hero">
      <div class="portrait" role="img" aria-label="Portrait photo of the speaker in an orange jacket standing at a dark podium with microphones"></div>
      <h1 class="name">Lori Mentaskel</h1>
      <span class="role row-1 col-a">Dynatmic Keynoter</span>
      <span class="role row-1 col-b">Motivating Speaker</span>
      <span class="role row-1 col-c">Influential Broadcaster</span>
      <span class="role row-2 col-a">Prolific Author</span>
      <span class="role row-2 col-b2">Enterainting Blogger</span>
      <span class="role row-2 col-c2">Effective Trainer</span>
      <div class="featured-band">
        <span class="featured-label">FEATURD ON</span>
        <div class="outlets">
          <span class="outlet">Ledgerline</span><span class="outlet">Morning Circle</span><span class="outlet">Trade Talk</span><span class="outlet">Metro 77</span><span class="outlet">Harbor 570</span><span class="outlet">Crestwave</span>
        </div>
      </div>
    </div>
  </section>
  <section class="header-variant second">
    <div class="nav-strip"></div>
    <div class="hero">
      <div class="portrait" role="img" aria-label="Portrait photo of the speaker in an orange jacket standing at a dark podium with microphones"></div>
      <h1 class="name">Lori Mentaskel</h1>
      <span class="role row-1 col-a">Dynatmic Keynoter</span>
      <span class="role row-1 col-b">Motivating Speaker</span>
      <span class="role row-1 col-c">Influential Broadcaster</span>
      <span class="role row-2 col-a">Prolific Author</span>
      <span class="role row-2 col-b2">Enterainting Blogger</span>
      <span class="role row-2 col-c2">Effective Trainer</span>
      <div class="featured-band">
        <span class="featured-label">FEATURD ON</span>
        <div class="outlets">
          <span class="outlet">Ledgerline</span><span class="outlet">Morning Circle</span><span class="outlet">Trade Talk</span><span class="outlet">Metro 77</span><span class="outlet">Harbor 570</span><span class="outlet">Crestwave</span>
        </div>
      </div>
    </div>
  </section>
</body>
</html>
```